Need Web Design for Business Process Outsourcing Company (Kelmora)

Kelmora is a business process outsourcing company. Need a simple site similar to http://www.tarvenholm.com/ but with a more professional and credible look. New to the process; not sure where to start and comparing my options. Please let me know what my options are if I choose to go with you. Logo is attached for your reference. Please use same colorway

Reason: I want the final product to be coded. Please confirm you will be able to code final design.

Industry/Entity Type

Business

Coding

Coded - Design and coding required

```html
<!DOCTYPE html>
<html lang="en">
<head>
<meta charset="utf-8">
<title>Kelmora Services</title>
<link href="https://fonts.googleapis.com/css2?family=Lato:wght@300;400;700&family=Raleway:wght@300;400;500;600&display=swap" rel="stylesheet">
<style>
:root{
  --blue:#0a8fd6;
  --blue-dark:#0866a6;
  --footer:#0b8fd4;
  --footer-bar:#0a5f98;
  --ink:#1d1d1d;
  --text:#6a6a6a;
  --line:#dcdcdc;
  --soft:#f3f3f3;
  --white:#ffffff;
}
*{margin:0;padding:0;box-sizing:border-box}
html,body{width:1200px;height:3158px;overflow:hidden}
body{font-family:"Lato",Arial,sans-serif;color:var(--text);background:var(--white);position:relative}
section,header,footer{position:absolute;left:0;width:1200px}
.abs{position:absolute}
.btn{position:absolute;background:var(--blue);color:var(--white);font-weight:700;text-transform:uppercase;display:flex;align-items:center;justify-content:center;border-radius:3px;border:2px solid var(--blue-dark)}

/* hero */
.hero{top:0;height:678px;background:linear-gradient(160deg,#f4f1f4 0%,#e9e6ee 35%,#dcd6e6 70%,#cfc6e1 100%)}
.hero-photo{position:absolute;inset:0;background:radial-gradient(ellipse at 50% 10%,rgba(255,255,255,.7),rgba(255,255,255,0) 60%),linear-gradient(90deg,rgba(190,180,205,.35),rgba(255,255,255,0) 30%,rgba(255,255,255,0) 70%,rgba(190,180,205,.35))}
.brand{position:absolute;left:76px;top:12px;display:flex;align-items:center;gap:10px;font-family:"Lato",sans-serif;font-weight:700;font-size:34px;color:var(--blue)}
.brand i{display:block;width:34px;height:34px;background:var(--blue);border-radius:4px}
.nav{position:absolute;left:368px;top:26px;display:flex;gap:0;font-size:16px;color:var(--ink);text-transform:uppercase}
.nav span{padding:0 12px 22px}
.nav .active{color:var(--blue);border-bottom:2px solid var(--blue)}
.nav-rule{position:absolute;left:368px;right:76px;top:72px;height:1px;background:rgba(0,0,0,.1)}
.hero-name{position:absolute;left:0;width:1200px;top:178px;text-align:center;font-weight:700;font-size:44px;color:var(--blue-dark)}
.hero h1{position:absolute;left:0;width:1200px;top:318px;text-align:center;font-family:"Raleway",sans-serif;font-weight:300;font-size:78px;color:#2a2a2a;letter-spacing:1px}
.hero h1 b{font-weight:500}
.hero p{position:absolute;left:240px;width:720px;top:426px;text-align:center;font-size:19px;line-height:25px;color:#444}
.hero .btn{left:470px;top:522px;width:260px;height:50px;font-size:18px;border-color:var(--blue-dark)}

/* services */
.services{top:678px;height:354px}
.section-title{position:absolute;left:0;width:1200px;text-align:center;font-family:"Raleway",sans-serif;font-size:40px;font-weight:500;color:var(--ink)}
.section-title b{font-weight:700}
.services .section-title{top:50px}
.service{position:absolute;top:178px;width:198px;height:125px;border:1px solid var(--line);border-radius:3px;text-align:center;box-shadow:0 1px 3px rgba(0,0,0,.06)}
.service .icon{position:absolute;left:62px;top:-36px;width:72px;height:72px;border-radius:50%;background:var(--blue);display:flex;align-items:center;justify-content:center}
.service h3{margin-top:52px;font-size:17px;font-weight:400;color:var(--ink);text-transform:uppercase}
.service p{font-size:12px;line-height:17px;margin:6px 28px 0}

/* features */
.features{top:1032px;height:343px;border-top:2px solid var(--blue);background:linear-gradient(180deg,#f1f7fb 0%,#e1eef6 45%,#d4e6f1 100%)}
.feature{position:absolute;width:290px}
.feature h3{font-size:19px;font-weight:400;color:var(--blue);text-transform:uppercase}
.feature p{font-size:14px;line-height:23px;margin-top:6px}
.feature.left{left:100px;text-align:right}
.feature.right{left:812px}
.f-icon{position:absolute}
.center-name{position:absolute;left:470px;width:260px;top:130px;text-align:center;font-size:58px;font-weight:700;color:var(--blue)}

/* news */
.news{top:1375px;height:457px}
.news .section-title{top:44px}
.post{position:absolute;top:115px;width:335px}
.post .photo{width:335px;height:167px}
.post .date{position:absolute;left:0;top:178px;width:53px;height:57px;background:var(--blue);color:var(--white);text-align:center;font-size:22px;line-height:24px;padding-top:5px}
.post .date small{display:block;font-size:17px}
.post .body{position:absolute;left:65px;top:176px;width:270px}
.post h4{font-size:15px;font-weight:400;color:var(--ink);line-height:20px}
.post p{font-size:13px;line-height:20px;margin-top:4px}
.post .more{font-size:14px;color:var(--blue);text-transform:uppercase;margin-top:6px}

/* presence */
.presence{top:1832px;height:678px;background:var(--soft)}
.presence h2{position:absolute;left:80px;top:54px;font-family:"Raleway",sans-serif;font-size:32px;font-weight:500;color:var(--blue);text-transform:uppercase}
.presence .intro{position:absolute;left:80px;top:105px;width:560px;font-size:14px;line-height:23px}
.presence .btn{left:78px;top:227px;width:126px;height:51px;font-size:15px}
.map{position:absolute;left:653px;top:20px;width:469px;height:295px;background:radial-gradient(ellipse at 50% 50%,#f0ddd4 0%,#f3ece8 55%,var(--soft) 80%)}
.divider{position:absolute;left:76px;right:76px;top:324px;height:1px;background:var(--line)}
.plant{position:absolute;left:42px;top:336px;width:505px;height:342px;background:radial-gradient(ellipse at 50% 55%,#6d9a38 0%,#8fb35a 30%,#e2e4dc 58%,var(--soft) 80%)}
.presence h2.pitch{left:562px;top:366px;width:560px;font-family:"Lato",sans-serif;font-size:30px;font-weight:400;text-transform:none;line-height:36px}
.presence .pitch-text{position:absolute;left:562px;top:443px;width:560px;font-size:14px;line-height:23px}
.presence .apply{left:562px;top:572px;width:156px;height:50px;font-size:15px}

/* contact */
.contact{top:2510px;height:374px}
.contact .section-title{top:54px;font-size:42px}
.field{position:absolute;height:53px;border:1px solid var(--line);border-radius:3px;display:flex;align-items:center;gap:12px;padding-left:14px;font-size:14px;color:#888}
.field.msg{align-items:flex-start;padding-top:14px}
.contact .btn{left:476px;top:273px;width:248px;height:51px;font-size:20px;font-weight:400}

/* footer */
.footer{top:2884px;height:274px;background:var(--footer);color:var(--white)}
.fcol{position:absolute;top:34px}
.fcol h5{font-size:18px;font-weight:400;text-transform:uppercase;margin-bottom:16px}
.fcol p{font-size:14px;line-height:23px}
.fline{display:flex;gap:14px;align-items:flex-start;font-size:14px;line-height:21px;margin-bottom:10px}
.fcol ul{list-style:none;font-size:14px;line-height:31px}
.fcol li::before{content:"•";margin-right:10px}
.foot-brand{position:absolute;left:912px;top:52px;width:190px;display:flex;align-items:center;gap:8px;font-size:30px;font-weight:700}
.foot-brand i{display:block;width:28px;height:28px;background:var(--white);border-radius:3px}
.socials{position:absolute;left:904px;top:120px;display:flex;gap:10px}
.socials span{width:40px;height:40px;border-radius:50%;border:2px solid rgba(255,255,255,.7)}
.socials span:first-child{background:var(--white)}
.footbar{position:absolute;left:0;top:221px;width:1200px;height:53px;background:var(--footer-bar);text-align:center;font-size:14px;line-height:53px}
.footbar em{font-style:normal;color:#7cc8f4}
.chat{position:absolute;left:1137px;top:3081px;width:46px;height:46px;border-radius:50%;background:var(--white);box-shadow:0 1px 4px rgba(0,0,0,.3);display:flex;align-items:center;justify-content:center}
</style>
</head>
<body>

<header class="hero">
  <div class="hero-photo" role="img" aria-label="Photo looking up at modern office towers against the sky"></div>
  <div class="brand"><i></i>Kelmora</div>
  <nav class="nav">
    <span class="active">Home</span><span>About</span><span>Services</span><span>Strategy</span><span>Experience</span><span>Security</span><span>News</span><span>Contact</span>
  </nav>
  <div class="nav-rule"></div>
  <div class="hero-name">Kelmora</div>
  <h1>We Offer <b>SOLUTIONS</b></h1>
  <p>Lorem Ipsum is simply dummy text of the printing and typesetting industry. Lorem Ipsum has been the industry's standard dummy text ever since the 1500s, when an unknown printer took a galley of type and scrambled it to make a type specimen book.</p>
  <a class="btn">Get a free quote</a>
</header>

<section class="services">
  <h2 class="section-title">Kelmora <b>SERVICES</b></h2>
  <div class="service" style="left:80px">
    <div class="icon"><svg width="38" height="38" viewBox="0 0 24 24" fill="none" stroke="#fff" stroke-width="1.8"><path d="M4 14v-2a8 8 0 0 1 16 0v2"/><rect x="3" y="13" width="4" height="6" rx="1"/><rect x="17" y="13" width="4" height="6" rx="1"/><path d="M19 19c0 2-3 3-6 3"/></svg></div>
    <h3>Customer Service</h3><p>Lorem Ipsum is simply dummy text of the printing.</p>
  </div>
  <div class="service" style="left:292px">
    <div class="icon"><svg width="38" height="38" viewBox="0 0 24 24" fill="none" stroke="#fff" stroke-width="1.8"><path d="M2 3h3l3 12h11l2-8H7"/><circle cx="9" cy="19" r="1.6"/><circle cx="17" cy="19" r="1.6"/></svg></div>
    <h3>Ecommerce</h3><p>Lorem Ipsum is simply dummy text of the printing.</p>
  </div>
  <div class="service" style="left:503px">
    <div class="icon"><svg width="38" height="38" viewBox="0 0 24 24" fill="none" stroke="#fff" stroke-width="1.8"><path d="M9 18h6M10 21h4M12 3a6 6 0 0 0-3.5 10.9V16h7v-2.1A6 6 0 0 0 12 3z"/><path d="M12 0v1M3 9H2M22 9h-1"/></svg></div>
    <h3>Creative</h3><p>Lorem Ipsum is simply dummy text of the printing.</p>
  </div>
  <div class="service" style="left:714px">
    <div class="icon"><svg width="38" height="38" viewBox="0 0 24 24" fill="none" stroke="#fff" stroke-width="1.8"><rect x="2" y="4" width="20" height="13" rx="1"/><path d="M8 21h8M12 17v4M6 13l4-4 3 3 5-5"/></svg></div>
    <h3>IT Solutions</h3><p>Lorem Ipsum is simply dummy text of the printing.</p>
  </div>
  <div class="service" style="left:926px">
    <div class="icon"><svg width="38" height="38" viewBox="0 0 24 24" fill="none" stroke="#fff" stroke-width="1.8"><circle cx="12" cy="7" r="3"/><path d="M6 20v-2a6 6 0 0 1 12 0v2"/><circle cx="4.5" cy="10" r="2"/><circle cx="19.5" cy="10" r="2"/></svg></div>
    <h3>Human Resources</h3><p>Lorem Ipsum is simply dummy text of the printing.</p>
  </div>
</section>

<section class="features" role="img" aria-label="Soft photo of a calm sea horizon behind the feature list">
  <div class="feature left" style="top:50px"><h3>Reinventing Services</h3><p>Lorem Ipsum is simply dummy text of the printing and typesetting industry. Lorem Ipsum has been the industry's standard.</p></div>
  <div class="feature left" style="top:186px"><h3>Success Stories</h3><p>Lorem Ipsum is simply dummy text of the printing and typesetting industry. Lorem Ipsum has been the industry's standard.</p></div>
  <div class="feature right" style="top:50px"><h3>Our Facilities</h3><p>Lorem Ipsum is simply dummy text of the printing and typesetting industry. Lorem Ipsum has been the industry's standard.</p></div>
  <div class="feature right" style="top:186px"><h3>Our People</h3><p>Lorem Ipsum is simply dummy text of the printing and typesetting industry. Lorem Ipsum has been the industry's standard.</p></div>
  <svg class="f-icon" style="left:404px;top:70px" width="70" height="64" viewBox="0 0 24 22" fill="#2b2b2b"><circle cx="8" cy="12" r="5"/><circle cx="18" cy="6" r="3.5"/><circle cx="18" cy="17" r="3"/><circle cx="8" cy="12" r="2" fill="#e6f0f6"/><circle cx="18" cy="6" r="1.4" fill="#e6f0f6"/><circle cx="18" cy="17" r="1.2" fill="#e6f0f6"/></svg>
  <svg class="f-icon" style="left:404px;top:204px" width="70" height="64" viewBox="0 0 24 22" fill="#2b2b2b"><rect x="2" y="15" width="3" height="7"/><rect x="7" y="12" width="3" height="10"/><rect x="12" y="14" width="3" height="8"/><rect x="17" y="9" width="3" height="13"/><path d="M2 11l6-5 4 3 8-7" stroke="#2b2b2b" stroke-width="1.6" fill="none"/><path d="M21 1v4h-4z"/></svg>
  <div class="center-name">Kelmora</div>
  <svg class="f-icon" style="left:726px;top:70px" width="62" height="64" viewBox="0 0 22 22" fill="#2b2b2b"><rect x="2" y="3" width="11" height="19"/><rect x="14" y="9" width="6" height="13"/><g fill="#e6f0f6"><rect x="4" y="6" width="2" height="2"/><rect x="9" y="6" width="2" height="2"/><rect x="4" y="11" width="2" height="2"/><rect x="9" y="11" width="2" height="2"/><rect x="4" y="16" width="2" height="2"/><rect x="9" y="16" width="2" height="2"/><rect x="16" y="12" width="2" height="2"/><rect x="16" y="17" width="2" height="2"/></g></svg>
  <svg class="f-icon" style="left:726px;top:204px" width="62" height="64" viewBox="0 0 22 22" fill="#2b2b2b"><circle cx="11" cy="6" r="4.5"/><path d="M2 22c0-6 4-9 9-9s9 3 9 9z"/><path d="M10 13h2l.6 6-1.6 2-1.6-2z" fill="#e6f0f6"/></svg>
</section>

<section class="news">
  <h2 class="section-title">Latest <b>NEWS</b></h2>
  <article class="post" style="left:76px">
    <div class="photo" role="img" aria-label="Photo of a person working on a laptop" style="background:linear-gradient(135deg,#c9ced6,#7d8694 60%,#4d5560)"></div>
    <div class="date">05<small>Apr</small></div>
    <div class="body"><h4>Lorem Ipsum is simply dummy text of the printing</h4><p>Lorem Ipsum is simply dummy text of the printing and typesetting industry.</p><div class="more">Read more</div></div>
  </article>
  <article class="post" style="left:432px">
    <div class="photo" role="img" aria-label="Photo of reading glasses resting on a printed page" style="background:linear-gradient(135deg,#f2f2f2,#d9d9d9 55%,#a78a6a)"></div>
    <div class="date">05<small>Apr</small></div>
    <div class="body"><h4>Lorem Ipsum is simply dummy text of the printing</h4><p>Lorem Ipsum is simply dummy text of the printing and typesetting industry.</p><div class="more">Read more</div></div>
  </article>
  <article class="post" style="left:787px">
    <div class="photo" role="img" aria-label="Photo of a business team meeting around a table" style="background:linear-gradient(135deg,#5c6c7a,#9aa8b2 50%,#e3e0d8)"></div>
    <div class="date">05<small>Apr</small></div>
    <div class="body"><h4>Lorem Ipsum is simply dummy text of the printing</h4><p>Lorem Ipsum is simply dummy text of the printing and typesetting industry.</p><div class="more">Read more</div></div>
  </article>
</section>

<section class="presence">
  <h2>Global Presence</h2>
  <p class="intro">Lorem Ipsum is simply dummy text of the printing and typesetting industry. Lorem Ipsum has been the industry's standard dummy text ever since the 1500s, when an unknown printer took a galley of type and scrambled it to make a type specimen book. It has survived not only five centuries, but also the leap into electronic typesetting, remaining essentially unchanged.</p>
  <a class="btn">Read more</a>
  <div class="map" role="img" aria-label="Illustrated world map with connected location pins"></div>
  <div class="divider"></div>
  <div class="plant" role="img" aria-label="Photo of a green seedling growing from a grass puzzle piece"></div>
  <h2 class="pitch">Passionate about engaging with clients and growing business?</h2>
  <p class="pitch-text">Lorem Ipsum is simply dummy text of the printing and typesetting industry. Lorem Ipsum has been the industry's standard dummy text ever since the 1500s, when an unknown printer took a galley of type and scrambled it to make a type specimen book. It has survived not only five centuries, but also the leap into electronic typesetting, remaining essentially unchanged.</p>
  <a class="btn apply">Apply with us!</a>
</section>

<section class="contact">
  <h2 class="section-title">Contact <b>US</b></h2>
  <div class="field" style="left:126px;top:115px;width:229px"><svg width="14" height="14" viewBox="0 0 24 24" fill="#8ab"><circle cx="12" cy="7" r="5"/><path d="M2 23c0-6 4-9 10-9s10 3 10 9z"/></svg>Your Name:</div>
  <div class="field" style="left:365px;top:115px;width:229px"><svg width="14" height="14" viewBox="0 0 24 24" fill="#555"><path d="M6 2l4 5-2 3a13 13 0 0 0 6 6l3-2 5 4-3 4C10 22 2 14 2 5z"/></svg>Phone No:</div>
  <div class="field" style="left:605px;top:115px;width:229px"><svg width="14" height="12" viewBox="0 0 24 18" fill="#555"><rect width="24" height="18" rx="2"/><path d="M1 1l11 9 11-9" stroke="#fff" stroke-width="2" fill="none"/></svg>E-Mail Address:</div>
  <div class="field" style="left:845px;top:115px;width:229px"><svg width="14" height="14" viewBox="0 0 24 24" fill="#555"><path d="M2 2h10l10 10-10 10L2 12z"/><circle cx="7" cy="7" r="2" fill="#fff"/></svg>Subject:</div>
  <div class="field msg" style="left:126px;top:178px;width:948px;height:84px"><svg width="14" height="14" viewBox="0 0 24 24" fill="#555"><path d="M3 21l2-6L17 3l4 4L9 19z"/></svg>Message:</div>
  <a class="btn">Request a quote</a>
</section>

<footer class="footer">
  <div class="fcol" style="left:80px;width:240px">
    <h5>About</h5>
    <p>Lorem Ipsum is simply dummy text of the printing and typesetting industry. Lorem Ipsum has been the industry's standard dummy text ever since the 1500s.</p>
  </div>
  <div class="fcol" style="left:370px;width:260px">
    <h5>Contact Us</h5>
    <div class="fline"><svg width="16" height="20" viewBox="0 0 16 20" fill="none" stroke="#fff" stroke-width="1.6"><path d="M8 19s6-6 6-11A6 6 0 0 0 2 8c0 5 6 11 6 11z"/><circle cx="8" cy="8" r="2"/></svg><span>123 Building Name, Street Name,<br>City, Country - zipcode</span></div>
    <div class="fline"><svg width="16" height="16" viewBox="0 0 24 24" fill="none" stroke="#fff" stroke-width="2"><path d="M6 2l4 5-2 3a13 13 0 0 0 6 6l3-2 5 4-3 4C10 22 2 14 2 5z"/></svg><span>123 4567 890</span></div>
    <div class="fline"><svg width="18" height="14" viewBox="0 0 24 18" fill="none" stroke="#fff" stroke-width="2"><rect x="1" y="1" width="22" height="16" rx="1"/><path d="M1 1l11 9 11-9"/></svg><span>info@kelmoraservices.com</span></div>
  </div>
  <div class="fcol" style="left:661px;width:220px">
    <h5>Useful Links</h5>
    <ul><li>Privacy Policy</li><li>Terms &amp; Conditions</li><li>Sitemap</li></ul>
  </div>
  <div class="foot-brand"><i></i>Kelmora</div>
  <div class="socials"><span></span><span></span><span></span><span></span></div>
  <div class="footbar">© <em>Kelmora SERVICES</em> - 2016. All Rights Reserved.</div>
</footer>

<div class="chat"><svg width="24" height="22" viewBox="0 0 24 22" fill="var(--blue)"><path d="M2 2h14v9H7l-4 3v-3H2z"/><path d="M18 6h4v9h-1v3l-4-3h-8v-2h9z"/></svg></div>

</body>
</html>
```